2025 Fall Auction

Large Farm and construction online only auction November 3rd thru 5Th
Bidding Closes November 5 th at 7 pm
Now Accepting Consignment call ( 555 )-712-3068 or email Marcus@velbrinauction.com
150 + Skid Steer Attachments
50 + Pieces of farm equipment
More To Come
Consignments are welcomed Till October 25Th

Target Market(s)

New customers

```html
<!DOCTYPE html>
<html lang="en">
<head>
<meta charset="utf-8">
<title>2025 Fall Auction – Large Farm &amp; Construction</title>
<link href="https://fonts.googleapis.com/css2?family=Oswald:wght@500;600&display=swap" rel="stylesheet">
<style>
  :root {
    --orange: #f7941e;
    --grey: #9b9b9b;
    --grey-text: #8c8c8c;
    --white: #ffffff;
    --sky-top: #a9c6de;
    --sky-low: #e8d9b8;
    --field: #6d9a3c;
    --machine-green: #3fae3a;
    --machine-dark: #1f2a22;
  }
  html, body {
    margin: 0;
    padding: 0;
    width: 831px;
    height: 1200px;
    overflow: hidden;
    background: var(--white);
  }
  .flyer { display: block; width: 831px; height: 1200px; }
  .flyer text { font-family: 'Oswald', sans-serif; font-weight: 500; }
  .brand-name { fill: var(--orange); font-size: 27px; }
  .year { fill: var(--grey); font-size: 88px; font-weight: 600; }
  .season-label { fill: var(--white); font-size: 30px; }
  .headline { fill: var(--orange); font-size: 66px; font-weight: 600; }
  .dates { fill: var(--white); font-size: 58px; }
  .closing { fill: var(--grey-text); font-size: 44px; }
  .consign-label { fill: var(--grey-text); font-size: 40px; }
  .contact-small { fill: var(--grey-text); font-size: 22px; }
  .contact-big { fill: var(--orange); font-size: 42px; }
  .highlight { fill: var(--white); font-size: 42px; }
  .deadline { fill: var(--grey-text); font-size: 44px; }
  .badge-text { fill: var(--white); font-size: 27px; font-weight: 600; }
</style>
</head>
<body>
<svg class="flyer" viewBox="0 0 831 1200" xmlns="http://www.w3.org/2000/svg">
  <defs>
    <linearGradient id="skyGrad" x1="0" y1="0" x2="0" y2="1">
      <stop offset="0" stop-color="var(--white)"/>
      <stop offset="0.35" stop-color="var(--sky-top)"/>
      <stop offset="0.8" stop-color="var(--sky-low)"/>
      <stop offset="1" stop-color="var(--field)"/>
    </linearGradient>
    <linearGradient id="machineGrad" x1="0" y1="0" x2="1" y2="1">
      <stop offset="0" stop-color="var(--machine-green)"/>
      <stop offset="0.6" stop-color="#2e8a2c"/>
      <stop offset="1" stop-color="var(--machine-dark)"/>
    </linearGradient>
  </defs>

  <!-- header scenery -->
  <rect class="scenery" x="0" y="138" width="831" height="300" fill="url(#skyGrad)" role="img" aria-label="Sky over a green field"/>
  <rect class="header-band" x="0" y="430" width="831" height="8" fill="var(--orange)"/>
  <circle class="header-arc" cx="532" cy="369" r="248" fill="var(--orange)"/>
  <rect class="machine-photo" x="330" y="56" width="501" height="340" rx="40" fill="url(#machineGrad)" role="img" aria-label="Photo of a large green farm tractor"/>

  <!-- brand -->
  <g class="brand">
    <circle cx="171" cy="108" r="56" fill="var(--orange)"/>
    <text class="brand-name" x="171" y="196" text-anchor="middle" textLength="190" lengthAdjust="spacingAndGlyphs">VELBRIN AUCTION SERVICE</text>
  </g>

  <!-- content panel -->
  <rect x="0" y="438" width="831" height="710" fill="var(--white)"/>
  <path class="panel-top" d="M66 438 V413 A48 48 0 0 1 114 365 H831 V438 Z" fill="var(--white)"/>

  <!-- badge -->
  <g class="badge" transform="translate(703 366)">
    <g fill="var(--orange)">
      <rect x="-66" y="-66" width="132" height="132"/>
      <rect x="-66" y="-66" width="132" height="132" transform="rotate(15)"/>
      <rect x="-66" y="-66" width="132" height="132" transform="rotate(30)"/>
      <rect x="-66" y="-66" width="132" height="132" transform="rotate(45)"/>
      <rect x="-66" y="-66" width="132" height="132" transform="rotate(60)"/>
      <rect x="-66" y="-66" width="132" height="132" transform="rotate(75)"/>
    </g>
    <circle r="71" fill="none" stroke="var(--white)" stroke-width="3"/>
    <g transform="rotate(12)">
      <text class="badge-text" x="0" y="-18" text-anchor="middle">ONLINE</text>
      <text class="badge-text" x="0" y="10" text-anchor="middle">ONLY</text>
      <text class="badge-text" x="0" y="38" text-anchor="middle">AUCTION</text>
    </g>
  </g>

  <!-- title -->
  <text class="year" x="105" y="491" textLength="170" lengthAdjust="spacingAndGlyphs">2025</text>
  <rect class="season-box" x="101" y="501" width="175" height="40" fill="var(--orange)"/>
  <text class="season-label" x="188" y="533" text-anchor="middle" textLength="165" lengthAdjust="spacingAndGlyphs">FALL AUCTION</text>
  <text class="headline" x="297" y="471" textLength="312" lengthAdjust="spacingAndGlyphs">LARGE FARM</text>
  <text class="headline" x="297" y="541" textLength="436" lengthAdjust="spacingAndGlyphs">&amp; CONSTRUCTION</text>

  <!-- dates -->
  <rect class="date-bar" x="89" y="562" width="652" height="80" rx="14" fill="var(--grey)"/>
  <text class="dates" x="415" y="626" text-anchor="middle" textLength="506" lengthAdjust="spacingAndGlyphs">November 3rd thru 5th</text>
  <text class="closing" x="415" y="703" text-anchor="middle" textLength="620" lengthAdjust="spacingAndGlyphs">Bidding Closes November 5th at 7 PM</text>
  <rect class="rule" x="89" y="726" width="652" height="3" fill="var(--orange)"/>

  <!-- consignments -->
  <text class="consign-label" x="107" y="787" textLength="220" lengthAdjust="spacingAndGlyphs">NOW ACCEPTING</text>
  <text class="consign-label" x="107" y="837" textLength="208" lengthAdjust="spacingAndGlyphs">CONSIGNMENTS</text>
  <rect class="divider" x="343" y="748" width="3" height="90" fill="var(--orange)"/>
  <text x="367" y="782"><tspan class="contact-small">Call </tspan><tspan class="contact-big">( 555 )-712-3068</tspan><tspan class="contact-small"> or email</tspan></text>
  <text class="contact-big" x="367" y="837" textLength="366" lengthAdjust="spacingAndGlyphs">Marcus@velbrinauction.com</text>

  <!-- highlights -->
  <rect class="highlights" x="89" y="858" width="652" height="175" rx="22" fill="var(--orange)"/>
  <g class="ticks" fill="none" stroke="var(--white)" stroke-width="5" stroke-linecap="round" stroke-linejoin="round">
    <path d="M134 893 l9 10 l16 -22"/>
    <path d="M134 943 l9 10 l16 -22"/>
    <path d="M134 993 l9 10 l16 -22"/>
  </g>
  <text class="highlight" x="173" y="910" textLength="430" lengthAdjust="spacingAndGlyphs">150+ Skid Steer Attachments</text>
  <text class="highlight" x="173" y="960" textLength="443" lengthAdjust="spacingAndGlyphs">50+ Pieces of Farm Equipment</text>
  <text class="highlight" x="173" y="1010" textLength="213" lengthAdjust="spacingAndGlyphs">More To Come!</text>

  <text class="deadline" x="415" y="1094" text-anchor="middle" textLength="636" lengthAdjust="spacingAndGlyphs">Consignments welcomed till October 25th</text>

  <rect class="footer-band" x="0" y="1146" width="831" height="54" fill="var(--orange)"/>
</svg>
</body>
</html>
```